Business cards/stationary for physician office
Using existing logo
Bright & Fun-filled
Paul Verner, M.D.
Radiologist
Cedarpoint Imaging, LLC.
48 Quill Ridge Lane
Montgomery, TX 77490
office@brakwell-mail.net
www.cedarpointimaging-demo.com
Will contact the winning designer with actual contact info to replace above text. Please not website has not been updated with new logo, so make sure to use provided logo files.
Logo files
Logo file horizontal

```html
<!DOCTYPE html>
<html lang="en">
<head>
<meta charset="utf-8">
<title>Cedarpoint Imaging – Business Card</title>
<link rel="stylesheet" href="https://fonts.googleapis.com/css2?family=Source+Sans+3:wght@400;600;700&display=swap">
<style>
  :root {
    --page-bg: #e9ebee;
    --card-white: #ffffff;
    --brand-blue: #2f5f9e;
    --brand-blue-dark: #234a7d;
    --swoosh-grey: #a9adb3;
    --swoosh-light: #d6d9dd;
    --ink-blue: #2f5f9e;
    --ink-dark: #1d2430;
    --ink-white: #ffffff;
  }
  * { box-sizing: border-box; margin: 0; padding: 0; }
  html, body {
    width: 1200px; height: 906px; overflow: hidden;
    background: var(--page-bg);
    font-family: "Source Sans 3", Arial, sans-serif;
  }
  .business-card {
    position: absolute; left: 180px; top: 213px;
    width: 840px; height: 480px;
    border-radius: 24px; overflow: hidden;
    background: var(--card-white);
    box-shadow: 0 10px 30px rgba(0,0,0,0.18);
  }
  .card-swoosh { position: absolute; inset: 0; width: 840px; height: 480px; }
  .doctor-block {
    position: absolute; right: 40px; top: 34px; text-align: right;
  }
  .doctor-name { font-size: 34px; font-weight: 400; color: var(--ink-blue); line-height: 1.1; }
  .doctor-title { font-size: 17px; font-weight: 700; color: var(--ink-dark); margin-top: 2px; }
  .brand-lockup {
    position: absolute; left: 44px; top: 196px;
    display: flex; align-items: center; gap: 16px;
  }
  .brand-dot {
    width: 64px; height: 64px; border-radius: 50%;
    background: var(--brand-blue);
  }
  .brand-name {
    font-size: 40px; font-weight: 600; color: var(--brand-blue);
    letter-spacing: 1px; text-transform: uppercase;
  }
  .contact-block {
    position: absolute; right: 40px; top: 214px;
    text-align: right; color: var(--ink-white);
    font-size: 18px; line-height: 1.33;
  }
  .contact-web {
    position: absolute; right: 40px; bottom: 26px;
    color: var(--ink-white); font-size: 18px;
  }
</style>
</head>
<body>
  <div class="business-card">
    <svg class="card-swoosh" viewBox="0 0 840 480" aria-hidden="true">
      <path d="M0,292 C250,372 520,272 620,192 C700,128 780,84 840,72 L840,480 L0,480 Z" fill="var(--swoosh-light)"/>
      <path d="M0,306 C255,388 530,288 630,206 C710,142 785,100 840,88 L840,480 L0,480 Z" fill="var(--swoosh-grey)"/>
      <path d="M0,330 C262,410 545,310 645,228 C725,164 792,124 840,114 L840,480 L0,480 Z" fill="var(--brand-blue)"/>
      <path d="M0,420 C300,470 560,420 840,330 L840,480 L0,480 Z" fill="var(--brand-blue-dark)" opacity="0.35"/>
    </svg>

    <div class="doctor-block">
      <div class="doctor-name">Paul Verner, M.D.</div>
      <div class="doctor-title">Radiologist</div>
    </div>

    <div class="brand-lockup">
      <div class="brand-dot"></div>
      <div class="brand-name">Cedarpoint Imaging</div>
    </div>

    <div class="contact-block">
      <div>Cedarpoint Imaging, LLC.</div>
      <div>48 Quill Ridge Lane</div>
      <div>Montgomery, TX 77490</div>
      <div>P : 936-555-0147</div>
      <div>C : 936-555-0183</div>
      <div>F : 936-555-0192</div>
      <div>E : office@brakwell-mail.net</div>
    </div>

    <div class="contact-web">W : www.cedarpointimaging-demo.com</div>
  </div>
</body>
</html>
```